New Business Card Design Project

The look of the business cards should include
-Clean Lines
-Should suit a sophisticated customer
-Evoke a mix of business and creativity
-Incorporate the color Gray or Black:White palette
-Open to see layouts in both vertical and horizontal
3 partners (we need 3 cards)
NORELLE VASK
ODA TRENCHARD
MARU ELDFORTH
Reason: We would like more submissions please
Target Market(s)
We are a NYC and European based boutique consulting agency specializing in fashion business and creative clients. In addition to consulting we will be offering an e-commerce site selling women’s accessories and jewelry geared towards fashion forward women ages 25-50.
Industry/Entity Type
Business
Font styles to use
Requirements
Must have
- - texture
- grayscale
3 Partners
Details for each card
CONSULTING I DESIGN
MARU ELDFORTH
Founding Partner
917.555.0183
maru@theplumwickhouse.com
www.theplumwickhouse.com
CONSULTING I DESIGN
NORELLE VASK
Founding Partner
917.555.0147
norelle@theplumwickhouse.com
www.theplumwickhouse.com
CONSULTING I DESIGN
Oda Kestlin Trenchard
Founding Partner
(no phone for her)
Oda@theplumwickhouse.com
www.theplumwickhouse.com

```html
<!DOCTYPE html>
<html lang="en">
<head>
<meta charset="utf-8">
<title>The Plumwick House — Business Cards</title>
<link rel="stylesheet" href="https://fonts.googleapis.com/css2?family=Montserrat:wght@300;400;700&display=swap">
<style>
  :root {
    --stage: #ecebe9;
    --card-gray: #5f5f5f;
    --card-gray-light: #6c6c6c;
    --card-gray-dark: #525252;
    --card-white: #ffffff;
    --ink: #1c1c1c;
    --ink-soft: #3a3a3a;
    --mark: #e9e9e9;
  }
  * { margin: 0; padding: 0; box-sizing: border-box; }
  html, body {
    width: 1200px;
    height: 1000px;
    overflow: hidden;
    background: var(--stage);
    font-family: "Montserrat", sans-serif;
  }
  .stage {
    position: relative;
    width: 1200px;
    height: 1000px;
  }
  .card {
    position: absolute;
    left: 250px;
    width: 700px;
    height: 400px;
    box-shadow: 0 14px 30px rgba(0,0,0,0.22), 0 2px 6px rgba(0,0,0,0.15);
    overflow: hidden;
  }
  .card--back { top: 70px; }
  .card--front { top: 530px; display: flex; }

  .textured {
    background:
      radial-gradient(ellipse at 30% 25%, rgba(255,255,255,0.08), transparent 60%),
      repeating-linear-gradient(45deg, rgba(255,255,255,0.018) 0 2px, rgba(0,0,0,0.018) 2px 4px),
      linear-gradient(160deg, var(--card-gray-light), var(--card-gray) 50%, var(--card-gray-dark));
  }
  .card--back { display: flex; align-items: center; justify-content: center; }

  .wordmark {
    color: var(--mark);
    font-weight: 300;
    text-transform: uppercase;
    text-align: center;
    line-height: 1.35;
  }
  .card--back .wordmark { font-size: 40px; letter-spacing: 0.32em; }

  .front-brand {
    width: 54%;
    height: 100%;
    display: flex;
    align-items: center;
    justify-content: center;
  }
  .front-brand .wordmark { font-size: 26px; letter-spacing: 0.3em; }

  .front-details {
    width: 46%;
    height: 100%;
    background: var(--card-white);
    padding: 92px 0 0 40px;
    color: var(--ink);
  }
  .services {
    font-size: 14px;
    font-weight: 400;
    letter-spacing: 0.04em;
    color: var(--ink-soft);
    margin-bottom: 14px;
  }
  .person-name {
    font-size: 21px;
    font-weight: 700;
    letter-spacing: 0.02em;
    margin-bottom: 2px;
  }
  .contact-line {
    font-size: 14.5px;
    font-weight: 400;
    line-height: 1.5;
    color: var(--ink-soft);
  }
  .website { margin-top: 26px; }
</style>
</head>
<body>
<main class="stage">
  <section class="card card--back textured" aria-label="Card back">
    <p class="wordmark">The<br>Plumwick<br>House</p>
  </section>

  <section class="card card--front" aria-label="Card front">
    <div class="front-brand textured">
      <p class="wordmark">The<br>Plumwick<br>House</p>
    </div>
    <div class="front-details">
      <p class="services">CONSULTING I DESIGN</p>
      <p class="person-name">MARU ELDFORTH</p>
      <p class="contact-line">Founding Partner</p>
      <p class="contact-line">917.555.0183</p>
      <p class="contact-line">maru@theplumwickhouse.com</p>
      <p class="contact-line website">www.theplumwickhouse.com</p>
    </div>
  </section>
</main>
</body>
</html>
```